Harlow Company Core Values

We are looking for an updated appearance to our Core Values with the addition of some descriptors to share with new hires, employees, and potential candidates

Requirements
Must have
• Core values and core value descriptors

```html
<!DOCTYPE html>
<html lang="en">
<head>
<meta charset="utf-8">
<title>Harlow Company – Our Core Values</title>
<link rel="stylesheet" href="https://fonts.googleapis.com/css2?family=Montserrat:wght@400;500&display=swap">
<style>
  :root {
    --brand-red: #a91f2c;
    --ink: #111111;
    --paper: #ffffff;
    --backdrop: #e9e8e7;
  }
  * { margin: 0; padding: 0; box-sizing: border-box; }
  html, body {
    width: 1200px;
    height: 1200px;
    overflow: hidden;
    background: var(--backdrop);
    font-family: "Montserrat", Arial, sans-serif;
  }
  .poster {
    position: absolute;
    left: 134px;
    top: 0;
    width: 932px;
    height: 1200px;
    background: var(--paper);
  }
  .company-name {
    position: absolute;
    left: 95px;
    top: 96px;
    font-size: 28px;
    font-weight: 400;
    line-height: 1;
    color: var(--ink);
  }
  .company-line {
    position: absolute;
    left: 96px;
    top: 133px;
    font-size: 11px;
    font-weight: 400;
    color: var(--brand-red);
    white-space: nowrap;
  }
  .value-badge {
    position: absolute;
    width: 186px;
    height: 186px;
    margin: -93px 0 0 -93px;
    border-radius: 50%;
    background: var(--brand-red);
  }
  .value-text {
    position: absolute;
    width: 280px;
    margin-left: -140px;
    text-align: center;
    white-space: nowrap;
  }
  .value-title {
    font-size: 19px;
    font-weight: 500;
    line-height: 21px;
    color: var(--ink);
  }
  .value-points { list-style: none; }
  .value-points li {
    font-size: 14.5px;
    line-height: 17px;
    color: var(--brand-red);
    margin-top: 2px;
  }
  .headline {
    position: absolute;
    left: 462px;
    top: 572px;
    transform: translateX(-50%);
    text-align: center;
    font-size: 55px;
    font-weight: 400;
    line-height: 66px;
    color: var(--ink);
    letter-spacing: 0.5px;
  }
</style>
</head>
<body>
<main class="poster">
  <div class="company-name">Harlow Company</div>
  <div class="company-line">Building Better Work Together Every Day</div>

  <h1 class="headline">OUR<br>CORE<br>VALUES</h1>

  <div class="value-badge" style="left:467px;top:271px" role="img" aria-label="Icon of a handshake forming a heart"></div>
  <div class="value-text" style="left:467px;top:375px">
    <h2 class="value-title">Respect Everyone</h2>
    <ul class="value-points">
      <li>Be kind</li>
      <li>Embrace each other’s<br>differences</li>
      <li>Healthy conflict</li>
    </ul>
  </div>

  <div class="value-badge" style="left:253px;top:393px" role="img" aria-label="Icon of an award medal with a star and ribbons"></div>
  <div class="value-text" style="left:253px;top:495px">
    <h2 class="value-title">Aim for excellence</h2>
    <ul class="value-points">
      <li>Learn from our mistakes</li>
      <li>Getting a little better everyday</li>
      <li>Life long Learner</li>
    </ul>
  </div>

  <div class="value-badge" style="left:679px;top:393px" role="img" aria-label="Icon of two caring hands around a heart"></div>
  <div class="value-text" style="left:679px;top:495px">
    <h2 class="value-title">Take Care</h2>
    <ul class="value-points">
      <li>Be safe</li>
      <li>Be well</li>
      <li>Look out for others</li>
    </ul>
  </div>

  <div class="value-badge" style="left:181px;top:689px" role="img" aria-label="Icon of two people exchanging speech bubbles"></div>
  <div class="value-text" style="left:181px;top:792px">
    <h2 class="value-title">Communicate</h2>
    <ul class="value-points">
      <li>Listen with intent</li>
      <li>Ask questions</li>
      <li>Think about delivery<br>of message</li>
    </ul>
  </div>

  <div class="value-badge" style="left:751px;top:689px" role="img" aria-label="Icon of balanced scales of justice"></div>
  <div class="value-text" style="left:751px;top:793px">
    <h2 class="value-title">Act Ethically</h2>
    <ul class="value-points">
      <li>Respect</li>
      <li>Doing the right<br>thing, even when no<br>one is looking</li>
      <li>Understand what<br>matters to others</li>
    </ul>
  </div>

  <div class="value-badge" style="left:346px;top:932px" role="img" aria-label="Icon of a heart with a flame inside"></div>
  <div class="value-text" style="left:346px;top:1036px">
    <h2 class="value-title">Share your passion</h2>
    <ul class="value-points">
      <li>Enjoy what you do</li>
      <li>Help others</li>
      <li>Positive outlook</li>
    </ul>
  </div>

  <div class="value-badge" style="left:585px;top:932px" role="img" aria-label="Icon of a glowing light bulb with a brain inside"></div>
  <div class="value-text" style="left:585px;top:1036px">
    <h2 class="value-title">Work Smart</h2>
    <ul class="value-points">
      <li>Choose priorities</li>
      <li>Focus</li>
      <li>Seek to understand</li>
    </ul>
  </div>
</main>
</body>
</html>
```